ALL TEXT Social Media Graphics

We are looking for a series of social media graphics for Instagram (new size: 4:5 (1080 x 1350 pixels) ratio that are ALL TEXT. We want the following quotes below on each graphic; one quote per graphic. AND, In very small letters at the bottom of each graphic, add @PaulaWrenLive
The look and feel of these graphics should be complimentary to the color palette attached below; but keep them simple. But the design is up to you; at the end of this document, I provided various samples of all text graphics that I like as examples.
The Quotes are in the attached WORD document
women trying to lose weight

```html
<!DOCTYPE html>
<html lang="en">
<head>
<meta charset="utf-8">
<title>Sunlit Body Shape-Up – Social Graphics</title>
<link href="https://fonts.googleapis.com/css2?family=Barlow:wght@500;600;700&family=Barlow+Condensed:wght@600;700;800&family=Bitter:wght@600;700;800&family=DM+Serif+Text&family=Rubik:wght@700;800;900&display=swap" rel="stylesheet">
<style>
  :root{
    --board:#5f5f5f;
    --card:#ffc0e3;
    --deep:#ad145a;
    --accent:#ec5f98;
    --soft:#f06ea3;
    --ink:#111;
  }
  *{box-sizing:border-box;margin:0;padding:0}
  html,body{width:1200px;height:594px;overflow:hidden;background:var(--board)}
  .board{position:relative;width:1200px;height:594px}
  .post{position:absolute;width:220px;height:275px;background:var(--card);padding:14px 15px 0 16px;overflow:hidden}
  .post p{margin:0}
  .handle{position:absolute;right:15px;bottom:12px;font:700 10px/1 "Barlow",sans-serif;color:var(--ink)}
  .c1{left:32.6px}.c2{left:261.3px}.c3{left:490px}.c4{left:718.7px}.c5{left:947.5px}
  .r1{top:17px}.r2{top:298px}

  .sans{font-family:"Barlow",sans-serif;font-weight:600}
  .cond{font-family:"Barlow Condensed",sans-serif;font-weight:800;letter-spacing:-.4px}
  .slab{font-family:"Bitter",serif;font-weight:800}
  .serif{font-family:"DM Serif Text",serif}
  .round{font-family:"Rubik",sans-serif;font-weight:800;letter-spacing:-.3px}
  .cta{font-family:"Barlow",sans-serif;font-weight:500;letter-spacing:.8px}
  .deep{color:var(--deep)} .accent{color:var(--accent)} .soft{color:var(--soft)}
</style>
</head>
<body>
<main class="board">

  <section class="post c1 r1">
    <p class="sans soft" style="font-size:19px;line-height:21.5px">You can absolutely be down 20–30 pounds by end of summer.</p>
    <p class="cond deep" style="font-size:31px;line-height:28.5px;margin-top:12px">All it takes is the right plan — and you’ve found it.</p>
    <p class="sans soft" style="font-size:16.5px;line-height:23px;margin-top:8px;font-weight:500">Comment “Sunlit” for the Sunlit Body Shape-Up!</p>
    <span class="handle">@PaulaWrenLive</span>
  </section>

  <section class="post c2 r1">
    <p class="cond soft" style="font-size:19.5px;line-height:22px;font-weight:700">You don’t need another diet — you need a system that works.</p>
    <p class="serif deep" style="font-size:27px;line-height:25.5px;margin-top:10px">Drop 30 pounds with the Sunlit Body Shape-Up.</p>
    <p class="cta soft" style="font-size:19px;line-height:20px;margin-top:8px">Comment “Summer” to start now.</p>
    <span class="handle">@PaulaWrenLive</span>
  </section>

  <section class="post c3 r1">
    <p class="cond deep" style="font-size:31px;line-height:27px">This summer ain’t over—and neither are your</p>
    <p class="slab soft" style="font-size:20px;line-height:23.5px;margin-top:10px;font-weight:700">Drop 30 pounds with the Sunlit Body Shape-Up.</p>
    <p class="cta deep" style="font-size:18.5px;line-height:20px;margin-top:10px">Comment “Sunlit” to get the plan</p>
    <span class="handle">@PaulaWrenLive</span>
  </section>

  <section class="post c4 r1">
    <p class="cond accent" style="font-size:27px;line-height:31px;font-weight:700">If your goal is a tiny waist,</p>
    <p class="cond accent" style="font-size:31px;line-height:33px">flat belly, and 30 pounds down</p>
    <p class="cond deep" style="font-size:25px;line-height:28px;margin-top:6px;font-weight:700">— this is the plan</p>
    <p class="cta soft" style="font-size:16px;line-height:19.5px;margin-top:6px;padding-left:4px">Comment “Summer” to join the Sunlit Body Shape-Up!</p>
    <span class="handle">@PaulaWrenLive</span>
  </section>

  <section class="post c5 r1">
    <p class="slab deep" style="font-size:26px;line-height:25.5px;font-weight:700">There’s still time to drop the 30 pounds and slay this summer.</p>
    <p class="cond accent" style="font-size:22px;line-height:22.5px;margin-top:8px;font-weight:700">The Sunlit Body Shape-Up has the blueprint.</p>
    <p class="cta soft" style="font-size:17px;line-height:20px;margin-top:5px">Comment “Sunlit”!</p>
    <span class="handle">@PaulaWrenLive</span>
  </section>

  <section class="post c1 r2">
    <p class="cond deep" style="font-size:23px;line-height:22.5px;font-weight:700">Snatched waist, flat tummy, 30 pounds lighter</p>
    <p class="cond accent" style="font-size:24px;line-height:25.5px;margin-top:8px">— that’s what the Sunlit Body Shape-Up Challenge delivers.</p>
    <p class="cta soft" style="font-size:18.5px;line-height:20px;margin-top:8px">Comment “Sunlit” to get the plan</p>
    <span class="handle">@PaulaWrenLive</span>
  </section>

  <section class="post c2 r2" style="padding-left:21px">
    <p class="round accent" style="font-size:21px;line-height:22.5px">Nothing feels better than seeing that scale drop week after week.</p>
    <p class="cond deep" style="font-size:14px;line-height:17px;margin-top:8px">Let’s lose up to 30 pounds this summer—together.</p>
    <p class="cta soft" style="font-size:16.5px;line-height:19.5px;margin-top:8px">Comment “Summer” to join the Sunlit Body Shape-Up!</p>
    <span class="handle">@PaulaWrenLive</span>
  </section>

  <section class="post c3 r2" style="padding-left:20px">
    <p class="cond deep" style="font-size:24px;line-height:27px">Sis, we’re dropping belly flat</p>
    <p class="round accent" style="font-size:28px;line-height:29px">and saying goodbye to stubborn pounds.</p>
    <p class="cta soft" style="font-size:16.5px;line-height:19.5px;margin-top:6px">Join the Sunlit Body Shape-Up</p>
    <p class="slab deep" style="font-size:15px;line-height:18px;margin-top:3px;padding-left:4px;font-weight:700">— comment “Summer”!</p>
    <span class="handle">@PaulaWrenLive</span>
  </section>

  <section class="post c4 r2" style="padding-left:17px">
    <p class="slab soft" style="font-size:25px;line-height:25px;font-weight:600">Don’t wait ‘til next summer to get right.</p>
    <p class="round deep" style="font-size:26px;line-height:26px;margin-top:6px">The time is</p>
    <p class="round deep" style="font-size:45px;line-height:38px;font-weight:900;letter-spacing:-1px">NOW.</p>
    <p class="slab accent" style="font-size:15.5px;line-height:16.5px;margin-top:4px;font-weight:700">Drop 30 pounds with the Sunlit Body Shape-Up.</p>
    <p class="slab deep" style="font-size:16px;line-height:20px;margin-top:5px;font-weight:700">Comment “Summer”!</p>
    <span class="handle">@PaulaWrenLive</span>
  </section>

  <section class="post c5 r2" style="padding-left:19px">
    <p class="slab deep" style="font-size:15px;line-height:19px;font-weight:600">You’ve got 8 weeks and</p>
    <p class="round accent" style="font-size:28px;line-height:30px;margin-top:2px">the perfect plan to drop 30 pounds</p>
    <p class="cond accent" style="font-size:21px;line-height:22.5px;margin-top:4px;font-weight:700">Let’s get snatched this summer with the Sunlit Body Shape-Up.</p>
    <p class="slab deep" style="font-size:16px;line-height:20px;margin-top:2px;font-weight:700">Comment “Summer”!</p>
    <span class="handle">@PaulaWrenLive</span>
  </section>

</main>
</body>
</html>
```